New letter head for Air Conditioning business

We need a new professional letter head design to suit our new re-branded air conditioning business. Our new logo is attached

```html
<!DOCTYPE html>
<html lang="en">
<head>
<meta charset="utf-8">
<title>Norvale Letterhead</title>
<link href="https://fonts.googleapis.com/css2?family=Questrial&display=swap" rel="stylesheet">
<style>
  :root {
    --backdrop: #d9d9d9;
    --paper: #ffffff;
    --charcoal: #3c3c3e;
    --mint: #5ec088;
    --coral: #ef6b5d;
    --ink: #2a2a2a;
    --signature-fill: #ececec;
  }
  * { margin: 0; padding: 0; box-sizing: border-box; }
  html, body {
    width: 1200px; height: 1159px; overflow: hidden;
    background: var(--backdrop);
    font-family: "Questrial", "Century Gothic", sans-serif;
  }
  .letterhead {
    position: absolute; left: 211px; top: 30px;
    width: 778px; height: 1100px;
    background: var(--paper);
    box-shadow: 0 6px 18px rgba(0,0,0,.25);
    overflow: hidden;
  }
  .header-wave { position: absolute; left: 0; top: 0; width: 778px; height: 260px; }
  .contact {
    position: absolute; right: 42px; top: 34px;
    color: #fff; font-size: 12px; line-height: 1.45;
    font-style: normal;
    text-align: right; letter-spacing: .3px;
  }
  .contact-line { display: flex; justify-content: flex-end; align-items: center; gap: 6px; }
  .contact-line svg { width: 10px; height: 10px; fill: var(--coral); }
  .contact-address { margin-bottom: 6px; }
  .brand {
    position: absolute; left: 48px; top: 250px;
    display: flex; align-items: center; gap: 12px;
  }
  .brand-dot { width: 34px; height: 34px; border-radius: 50%; background: var(--mint); }
  .brand-name {
    font-size: 40px; color: var(--charcoal); letter-spacing: 4px;
    text-transform: uppercase;
  }
  .letter-body {
    position: absolute; left: 100px; top: 380px; width: 600px;
    color: var(--ink); font-size: 14px; line-height: 1.55;
  }
  .recipient { margin-bottom: 16px; }
  .letter-body p.paragraph { margin-bottom: 20px; }
  .closing { margin-top: 6px; }
  .signature {
    width: 150px; height: 56px; margin-top: 16px;
    background: var(--signature-fill); border-radius: 4px;
  }
</style>
</head>
<body>
  <main class="letterhead">
    <svg class="header-wave" viewBox="0 0 778 260" aria-hidden="true">
      <path d="M0,0 H778 V132 C730,210 600,205 440,175 C270,142 110,120 0,222 Z" fill="var(--coral)"/>
      <path d="M0,0 H778 V124 C730,198 600,196 440,168 C270,136 110,114 0,214 Z" fill="var(--mint)"/>
      <path d="M0,0 H778 V112 C728,184 600,186 440,160 C270,130 110,108 0,206 Z" fill="var(--charcoal)"/>
    </svg>

    <address class="contact">
      <div class="contact-address">4810 Alder Creek Road, Suite 210<br>Linwood, CA 92090</div>
      <div class="contact-line">555-014-2731
        <svg viewBox="0 0 10 10"><path d="M2 0.5 L4 2.5 L3 3.8 Q4.5 6 6.2 7 L7.5 6 L9.5 8 L8 9.5 Q3 9 0.5 2 Z"/></svg></div>
      <div class="contact-line">555-014-8860
        <svg viewBox="0 0 10 10"><rect x="2" y="0.5" width="6" height="3"/><rect x="0.5" y="3.5" width="9" height="4" rx="1"/><rect x="2" y="7" width="6" height="2.5"/></svg></div>
      <div class="contact-line">info@norvaleair.com
        <svg viewBox="0 0 10 10"><path d="M0.5 2 H9.5 V8.5 H0.5 Z M0.5 2 L5 5.5 L9.5 2" stroke="#fff" stroke-width=".6"/></svg></div>
      <div class="contact-line">www.norvaleair.com
        <svg viewBox="0 0 10 10"><circle cx="5" cy="5" r="4.5"/></svg></div>
    </address>

    <div class="brand">
      <span class="brand-dot"></span>
      <span class="brand-name">Norvale</span>
    </div>

    <section class="letter-body">
      <div class="recipient">
        Mr/s<br>First Name and Last Name<br>Company Name<br>Address
      </div>
      <p class="paragraph">Lorem Ipsum is simply dummy text of the printing and typesetting industry. Lorem Ipsum has been the industry's standard dummy text ever since the 1500s, when an unknown printer took a galley of type and scrambled it to make a type specimen book. It has survived not only five centuries, but also the leap into electronic typesetting, remaining essentially unchanged. It was popularised in the 1960s with the release of Transfera sheets containing Lorem Ipsum passages.</p>
      <p class="paragraph">The standard chunk of Lorem Ipsum used since the 1500s is reproduced below for those interested. Sections 1.10.32 and 1.10.33 from "de Rebus Communibus" by Aurelo Vant are also reproduced in their exact original form, accompanied by English versions from the 1914 translation by J. Welford. Lorem ipsum dolor sit amet, consectetur adipiscing elit, sed do eiusmod tempor incididunt ut labore et dolore magna aliqua.</p>
      <p class="paragraph">It is a long established fact that a reader will be distracted by the readable content of a page when looking at its layout. The point of using Lorem Ipsum is that it has a more-or-less normal distribution of letters, as opposed to using 'Content here, content here', making it look like readable English. Many desktop publishing packages and web page editors now.</p>
      <p class="closing">Your Sincerely,</p>
      <div class="signature" role="img" aria-label="Handwritten signature"></div>
    </section>
  </main>
</body>
</html>
```